Design some Business Card for shipping company

We need a creative business card designed for a shipping company. All relevant information such as address and phone number can be found on our website. Will need a design for both front and back. The front will container our logo, slogan, contact information etc. The back will have a coupon and some text. check out www.taldovefreight.example for all the information. We need something memorable and unique that will stand out. It needs to a horizontal design. Not vertical.

```html
<!DOCTYPE html>
<html lang="en">
<head>
<meta charset="utf-8">
<title>Taldove Freight – Business Cards</title>
<link rel="stylesheet" href="https://fonts.googleapis.com/css2?family=Open+Sans:wght@400;600;700;800&display=swap">
<style>
  :root{
    --bg:#e6e6e4;
    --card:#ffffff;
    --green:#1f8a3b;
    --red:#c8202f;
    --black:#141414;
    --ink:#2b2b2b;
    --coupon:#eeeeee;
    --edge:#3a6ea5;
  }
  *{margin:0;padding:0;box-sizing:border-box}
  html,body{width:1200px;height:1053px;overflow:hidden;background:var(--bg);font-family:"Open Sans",sans-serif;color:var(--ink)}
  .sheet{position:relative;width:1200px;height:1053px}
  .card{position:absolute;left:250px;width:700px;height:400px;background:var(--card);overflow:hidden;box-shadow:0 6px 18px rgba(0,0,0,.18)}
  .card--back{top:70px}
  .card--front{top:560px;border-bottom:6px solid var(--edge)}
  .brand-name{font-weight:800;color:var(--green);text-transform:uppercase;letter-spacing:.02em;line-height:1}
  .slogan{font-weight:800;color:var(--black);line-height:1.2}
  .url{font-size:13px;color:var(--ink)}
  .stripes{position:absolute;display:block}

  /* back */
  .back-brand{position:absolute;left:40px;top:52px;display:flex;align-items:center;gap:12px}
  .back-brand .mark{width:40px;height:40px;border-radius:50%;background:var(--green)}
  .back-brand .brand-name{font-size:26px}
  .back-brand .slogan{font-size:13px;margin-top:4px}
  .card--back .stripes{left:0;top:118px}
  .top-rule{position:absolute;right:0;top:26px;width:300px;height:3px;background:var(--green)}
  .contact{position:absolute;left:400px;top:42px;font-size:13px;line-height:1.45}
  .contact h3{font-size:13px;font-weight:700;color:var(--red);text-transform:uppercase;letter-spacing:.02em}
  .contact h3 + p{margin-bottom:6px}
  .coupon{position:absolute;left:40px;top:200px;width:620px;height:150px;background:var(--coupon)}
  .card--back .url{position:absolute;left:40px;bottom:18px}

  /* front */
  .front-mark{position:absolute;left:50%;top:50px;width:110px;height:110px;margin-left:-55px;border-radius:50%;background:var(--green)}
  .front-text{position:absolute;left:0;right:0;top:185px;text-align:center}
  .front-text .brand-name{font-size:42px}
  .front-text .slogan{font-size:19px;margin-top:6px}
  .front-text .url{margin-top:8px}
  .card--front .stripes{left:0;bottom:26px}
</style>
</head>
<body>
<main class="sheet">

  <section class="card card--back" aria-label="Card back">
    <div class="back-brand">
      <span class="mark"></span>
      <div>
        <div class="brand-name">Taldove Freight</div>
        <div class="slogan">Secure Affordable Shipping to Kenya</div>
      </div>
    </div>
    <svg class="stripes" width="320" height="60" viewBox="0 0 320 60" aria-hidden="true">
      <polygon points="0,0 310,0 300,10 0,10" fill="var(--green)"/>
      <polygon points="0,20 250,20 240,32 0,32" fill="var(--red)"/>
      <polygon points="0,42 190,42 180,54 0,54" fill="var(--black)"/>
    </svg>
    <div class="top-rule"></div>
    <div class="contact">
      <h3>Contact Us</h3>
      <p>USA: Tel: +1 555 014 2290<br>KENYA: +254700318642, 0700318642</p>
      <h3>Our Shipping Address</h3>
      <p>1480 Harbor Crest Ave NE<br>Unit #310<br>Lakemont WA 98010</p>
    </div>
    <div class="coupon"></div>
    <div class="url">www.taldovefreight.example/</div>
  </section>

  <section class="card card--front" aria-label="Card front">
    <div class="front-mark"></div>
    <div class="front-text">
      <div class="brand-name">Taldove Freight</div>
      <div class="slogan">Secure Affordable Shipping to Kenya</div>
      <div class="url">www.taldovefreight.example/</div>
    </div>
    <svg class="stripes" width="520" height="56" viewBox="0 0 520 56" aria-hidden="true">
      <polygon points="0,0 510,0 498,12 0,12" fill="var(--green)"/>
      <polygon points="0,20 430,20 418,32 0,32" fill="var(--red)"/>
      <polygon points="0,40 350,40 338,52 0,52" fill="var(--black)"/>
    </svg>
  </section>

</main>
</body>
</html>
```